Website for Cannabis Investment Fund *

We need to create a website for our fund which invests in cannabis projects

Industry/Entity Type

Cannabis

Coding

Coded - Design and coding required

Number of Pages Required

1 page

Colors

Designer to choose only greyscale colors for use in the design.

Requirements
Must have
• Please see the attached file

```html
<!DOCTYPE html>
<html lang="en">
<head>
<meta charset="utf-8">
<title>VerdaLeaf Capital</title>
<link href="https://fonts.googleapis.com/css2?family=Montserrat:wght@400;500;600;700&family=Open+Sans:wght@400;600&display=swap" rel="stylesheet">
<style>
:root{
  --green:#1f6b4a;
  --green-dark:#175a3d;
  --green-bright:#3aa63a;
  --ink:#1e1e1e;
  --text:#444;
  --muted:#8a8a8a;
  --line:#c8c8c8;
  --white:#fff;
  --footer:#242424;
}
*{margin:0;padding:0;box-sizing:border-box}
html,body{width:1200px;height:2969px;overflow:hidden}
body{position:relative;background:var(--white);font-family:'Open Sans',sans-serif;color:var(--text)}
.abs{position:absolute}
.center{left:0;width:1200px;text-align:center}

/* hero */
.hero{top:0;left:0;width:1200px;height:692px;background:radial-gradient(ellipse at 50% 30%,#2d5a2c 0%,#1b3a1d 45%,#0f1a12 100%)}
.hero-cut{position:absolute;top:0;left:0}
.brand{top:26px;left:144px;font-family:'Montserrat',sans-serif;font-weight:700;font-size:25px;color:var(--white);display:flex;align-items:center;gap:8px}
.brand-dot{width:12px;height:12px;border-radius:50%;background:var(--green-bright)}
.nav{top:32px;left:680px;display:flex;gap:33px;font-family:'Montserrat',sans-serif;font-size:13px;color:var(--white)}
.nav .active{text-decoration:underline;text-underline-offset:4px}
.lang{top:34px;left:1030px;width:16px;height:11px;background:#3b4aa0;border:1px solid #ddd}
.hero-title{top:258px;font-family:'Montserrat',sans-serif;font-weight:600;font-size:21px;line-height:31px;color:var(--white)}
.btn-outline{top:334px;left:532px;width:136px;height:40px;border:1px solid var(--white);border-radius:20px;color:var(--white);font-family:'Montserrat',sans-serif;font-weight:600;font-size:13px;line-height:38px;text-align:center}

/* value chain */
.chain-title{top:753px;font-family:'Montserrat',sans-serif;font-weight:500;font-size:21px;color:var(--ink)}
.chain-art{top:0;left:0}
.step-label{width:240px;left:480px;text-align:center;font-family:'Montserrat',sans-serif;font-size:18px;line-height:24px;color:var(--ink)}
.step-note{font-size:13px;line-height:21px;color:var(--text);width:262px}
.step-note.left{left:141px;text-align:right}
.step-note.right{left:801px;text-align:left}

/* team */
.team{top:1638px;left:0;width:1200px;height:576px;background:linear-gradient(120deg,#1c6645 0%,#237a54 55%,#1a5f40 100%)}
.team-title{top:1712px;font-family:'Montserrat',sans-serif;font-weight:600;font-size:33px;color:var(--white)}
.team-sub{top:1752px;font-size:13px;color:#a9d3bd}
.team-filter{top:1786px;font-family:'Montserrat',sans-serif;font-size:16px;color:var(--white)}
.team-filter .on{text-decoration:underline;text-underline-offset:4px}
.team-filter .sep{margin:0 12px}
.member{top:1833px;width:303px;height:302px;background:linear-gradient(160deg,#9c9c98 0%,#6e6c68 60%,#4d4b48 100%)}
.member.hover{background:linear-gradient(160deg,#5a5856 0%,#403e3c 100%)}
.member-name{position:absolute;top:118px;width:100%;text-align:center;font-family:'Montserrat',sans-serif;font-weight:600;font-size:23px;color:var(--white)}
.member-role{position:absolute;top:150px;width:100%;text-align:center;font-size:10px;color:var(--white)}
.member-go{position:absolute;top:166px;left:141px;width:20px;height:20px;border-radius:50%;background:var(--white)}

/* contact */
.contact{top:2214px;left:0;width:1200px;height:400px;background:radial-gradient(ellipse at 60% 30%,#d9d9d9 0%,#e9e9e9 50%,#eeeeee 100%)}
.contact-title{top:2343px;font-family:'Montserrat',sans-serif;font-weight:600;font-size:33px;color:var(--green)}
.contact-sub{top:2396px;font-size:13px;color:var(--text)}
.btn{top:2438px;width:136px;height:39px;line-height:39px;text-align:center;font-family:'Montserrat',sans-serif;font-size:13px;color:var(--white)}
.btn.primary{left:455px;background:var(--green)}
.btn.dark{left:607px;background:var(--ink)}

/* info */
.info-title{top:2686px;font-family:'Montserrat',sans-serif;font-weight:600;font-size:33px;color:var(--green)}
.info-item{top:2748px;width:320px;text-align:center;font-family:'Montserrat',sans-serif;font-size:13px;color:var(--ink)}
.info-item svg{display:block;margin:0 auto 6px}

/* footer */
.footer{top:2874px;left:0;width:1200px;height:95px;background:var(--footer)}
.foot-links{top:2897px;left:144px;font-size:11px;color:#bdbdbd}
.foot-links .sep{margin:0 8px}
.foot-copy{top:2927px;left:144px;font-size:11px;color:#bdbdbd}
.social{top:2913px;width:14px;height:14px;border-radius:50%;background:#8a8a8a}
</style>
</head>
<body>

<section class="abs hero" role="img" aria-label="Close-up photograph of cannabis leaves on a dark background"></section>
<svg class="hero-cut" width="1200" height="700"><polygon points="0,693 600,582 1200,693 1200,700 0,700" fill="#fff"/></svg>

<div class="abs brand"><span class="brand-dot"></span>VerdaLeaf Capital</div>
<nav class="abs nav"><span class="active">INVESTMENT FOCUS</span><span>TEAM</span><span>CONTACT US</span></nav>
<div class="abs lang"></div>
<h1 class="abs center hero-title">Or goal is to leverage growth of the global cannabis industry by<br>investing in public and private equity of companies in this sector</h1>
<div class="abs btn-outline">EXPLORE MORE</div>

<h2 class="abs center chain-title">We invest across all steps of the cannabis-product value chain</h2>

<svg class="abs chain-art" width="1200" height="1600" fill="none">
  <g stroke="#9a9a9a" stroke-width="2">
    <line x1="600" y1="788" x2="600" y2="826"/>
    <line x1="600" y1="966" x2="600" y2="1004"/>
    <line x1="600" y1="1143" x2="600" y2="1181"/>
    <line x1="600" y1="1342" x2="600" y2="1380"/>
    <line x1="600" y1="1518" x2="600" y2="1557"/>
  </g>
  <g stroke="#bdbdbd" stroke-width="1">
    <polyline points="424,840 476,935 516,935"/>
    <polyline points="773,1018 722,1112 682,1112"/>
    <polyline points="424,1219 476,1313 516,1313"/>
    <polyline points="773,1396 722,1491 682,1491"/>
  </g>
  <g>
    <circle cx="424" cy="840" r="11" fill="#b6d8c4"/><circle cx="424" cy="840" r="7" fill="#1f6b4a"/>
    <circle cx="773" cy="1018" r="11" fill="#b6d8c4"/><circle cx="773" cy="1018" r="7" fill="#1f6b4a"/>
    <circle cx="424" cy="1219" r="11" fill="#b6d8c4"/><circle cx="424" cy="1219" r="7" fill="#1f6b4a"/>
    <circle cx="773" cy="1396" r="11" fill="#b6d8c4"/><circle cx="773" cy="1396" r="7" fill="#1f6b4a"/>
  </g>
  <g stroke="#8a8a8a" stroke-width="1">
    <circle cx="600" cy="873" r="40"/>
    <circle cx="600" cy="1050" r="40"/>
    <circle cx="600" cy="1227" r="40"/>
    <circle cx="600" cy="1428" r="40"/>
  </g>
  <g stroke="#1f6b4a" stroke-width="1.6" stroke-linejoin="round">
    <!-- tractor -->
    <circle cx="589" cy="887" r="6"/><circle cx="612" cy="884" r="9"/><circle cx="612" cy="884" r="3"/>
    <path d="M580 884v-12h16l3-10h12l2 13"/><line x1="602" y1="862" x2="602" y2="874"/>
    <!-- leaf -->
    <path d="M600 1066v-28M600 1038c-4 8-4 18 0 26c4-8 4-18 0-26zM600 1062c-8-2-14-8-16-16c8 2 14 8 16 16zM600 1062c8-2 14-8 16-16c-8 2-14 8-16 16z"/>
    <!-- box -->
    <path d="M582 1216l18-8 18 8v22l-18 8-18-8z"/><path d="M582 1216l18 8 18-8M600 1224v22M591 1212l18 8"/>
    <!-- truck -->
    <path d="M576 1414h30v24h-30zM606 1422h12l6 8v8h-18"/>
    <circle cx="586" cy="1440" r="4" fill="#fff"/><circle cx="614" cy="1440" r="4" fill="#fff"/>
  </g>
</svg>

<div class="abs step-label" style="top:923px">Cultivation</div>
<div class="abs step-label" style="top:1100px">Processing</div>
<div class="abs step-label" style="top:1277px">Value added<br>retail products</div>
<div class="abs step-label" style="top:1478px">Distribution</div>

<p class="abs step-note left" style="top:828px">Cultivation facilities –high tech greenhouses aimed to reduce operational costs and maximize quality of flowers and pre-rolls</p>
<p class="abs step-note right" style="top:1005px">High quality THC and CBD concentrates used for the enrichment of FMCG or medical end products as well as concentrates available for The direct retail consumption (such as oil and powders)</p>
<p class="abs step-note left" style="top:1207px">Value added products in several sectors: Health and Beauty, Pharmaceutical products, food and beverages</p>
<p class="abs step-note right" style="top:1383px">Promising tools of distribution within the cannabis industry: e-shops, coffee shop branches etc.</p>

<section class="abs team"></section>
<h2 class="abs center team-title">OUR TEAM</h2>
<p class="abs center team-sub">Pellentesque risus dolor, tristique vel facilisis at, laoreet ut elit.</p>
<div class="abs center team-filter"><span class="on">All</span><span class="sep">/</span>Investment Team<span class="sep">/</span>Advisory Board</div>
<div class="abs member" style="left:144px" role="img" aria-label="Portrait photo of an investment team member"></div>
<div class="abs member" style="left:448px" role="img" aria-label="Portrait photo of an investment team member"></div>
<div class="abs member hover" style="left:752px" role="img" aria-label="Portrait photo of Mark Hale">
  <div class="member-name">MARK HALE</div>
  <div class="member-role">Curabitur non risus sed</div>
  <svg class="member-go" viewBox="0 0 20 20"><path d="M8 5l5 5-5 5" stroke="#404040" stroke-width="2" fill="none"/></svg>
</div>

<section class="abs contact" role="img" aria-label="Faded greyscale photograph of cannabis leaves"></section>
<h2 class="abs center contact-title">CONTACT US</h2>
<p class="abs center contact-sub">Fusce sodales, odio eget egestas faucibus, ex dolor lacinia diam</p>
<div class="abs btn primary">SEND MESSAGE</div>
<div class="abs btn dark">INVESTORS</div>

<h2 class="abs center info-title">CONTACT INFO</h2>
<div class="abs info-item" style="left:128px">
  <svg width="28" height="28" viewBox="0 0 24 24"><path d="M6.6 10.8a15 15 0 0 0 6.6 6.6l2.2-2.2c.3-.3.7-.4 1-.2 1.1.4 2.3.6 3.6.6.6 0 1 .4 1 1V20c0 .6-.4 1-1 1A17 17 0 0 1 3 4c0-.6.4-1 1-1h3.5c.6 0 1 .4 1 1 0 1.3.2 2.5.6 3.6.1.3 0 .7-.2 1z" fill="#8a8a8a"/></svg>
  555 210 4837</div>
<div class="abs info-item" style="left:440px">
  <svg width="28" height="28" viewBox="0 0 24 24"><path d="M12 2a7 7 0 0 0-7 7c0 5 7 13 7 13s7-8 7-13a7 7 0 0 0-7-7zm0 9.5a2.5 2.5 0 1 1 0-5 2.5 2.5 0 0 1 0 5z" fill="#8a8a8a"/></svg>
  24 Building name, Street name, City Zipcode</div>
<div class="abs info-item" style="left:751px">
  <svg width="32" height="28" viewBox="0 0 32 24"><rect x="1" y="3" width="30" height="20" rx="2" fill="#8a8a8a"/><path d="M2 5l14 10 14-10" stroke="#fff" stroke-width="2" fill="none"/></svg>
  info@verdaleaf.example</div>

<footer class="abs footer"></footer>
<div class="abs foot-links">Investment Focus<span class="sep">|</span>Team<span class="sep">|</span>Contact Us</div>
<div class="abs foot-copy">Copyright © 2019 VerdaLeaf Capital. All rights reserved.</div>
<div class="abs social" style="left:1004px"></div>
<div class="abs social" style="left:1039px"></div>

</body>
</html>
```